The Copper Lantern is a traditional English pub serving a vast range of beers and real ales. It has a very conservative oulook. Something classy would work well. We have an in-house logo. I'm thinking of good quality card in say cream with matching compliment slips and headed paper and envelopes

Industry/Entity Type

Conservative

Contact Information for Business Card

Copper Lantern Public House
58 Mill Lane
Ashvale
Middlesex
TW9 3RK
Derek P Lowther - Proprietor
www.copperlanternvale.co.uk
Tel: 020 7946 0382
Mobile; 077009 00415

Requirements
Must have
• Cl design essential. Black text.

2 sets of business cards required. one set must have my name - Derek P Lowther - Proprietor and the second set should have - Maureen Fitch - General Manager

```html
<!DOCTYPE html>
<html lang="en">
<head>
<meta charset="utf-8">
<title>Copper Lantern – Business Card</title>
<link href="https://fonts.googleapis.com/css2?family=Didact+Gothic&display=swap" rel="stylesheet">
<style>
  :root {
    --page-bg: #e6e6e4;
    --wood-dark: #4a3322;
    --wood-mid: #7a5a3c;
    --wood-light: #9c7a55;
    --band-white: #ffffff;
    --panel-black: #060606;
    --ink-black: #111111;
    --ink-white: #f2f2f2;
  }
  * { margin: 0; padding: 0; box-sizing: border-box; }
  html, body {
    width: 1200px;
    height: 899px;
    overflow: hidden;
    background: var(--page-bg);
    font-family: "Didact Gothic", "Helvetica Neue", Arial, sans-serif;
  }
  .canvas {
    position: relative;
    width: 1200px;
    height: 899px;
    display: flex;
    align-items: center;
    justify-content: center;
  }
  .business-card {
    position: relative;
    width: 1000px;
    height: 620px;
    overflow: hidden;
    box-shadow: 0 10px 30px rgba(0,0,0,0.18);
  }
  .wood-texture {
    position: absolute;
    inset: 0;
    background:
      linear-gradient(180deg, rgba(0,0,0,0.12) 0%, rgba(255,255,255,0.05) 30%, rgba(0,0,0,0.15) 60%, rgba(255,255,255,0.04) 80%, rgba(0,0,0,0.2) 100%),
      linear-gradient(90deg, var(--wood-dark) 0%, var(--wood-mid) 25%, var(--wood-light) 50%, var(--wood-mid) 75%, var(--wood-dark) 100%);
  }
  .block { position: absolute; }
  .block--black { background: var(--panel-black); }
  .block--white { background: var(--band-white); }

  .top-left-block  { left: 40px;  top: 70px; width: 230px; height: 90px; }
  .logo-band       { left: 270px; top: 50px; width: 330px; height: 110px; }
  .top-right-block { left: 600px; top: 40px; width: 230px; height: 80px; }
  .logo-extension  { left: 600px; top: 120px; width: 360px; height: 40px; }

  .logo {
    position: absolute;
    inset: 0;
    display: flex;
    align-items: center;
    justify-content: center;
    gap: 14px;
    color: var(--ink-black);
  }
  .logo-dot {
    width: 44px;
    height: 44px;
    border-radius: 50%;
    background: var(--ink-black);
    flex: none;
  }
  .logo-name {
    font-size: 34px;
    line-height: 1;
    letter-spacing: 1px;
    text-transform: uppercase;
  }

  .name-band {
    left: 40px; top: 200px; width: 920px; height: 96px;
    display: flex; align-items: center; padding-left: 70px;
  }
  .name-title {
    font-size: 40px;
    color: var(--ink-black);
    letter-spacing: 0.5px;
  }

  .contact-panel {
    left: 40px; top: 330px; width: 920px; height: 240px;
    display: flex;
    justify-content: space-between;
    padding: 40px 70px 0 60px;
    color: var(--ink-white);
    font-size: 25px;
    line-height: 2.05;
  }
  .contact-panel p { white-space: nowrap; }
  .contact-column--right { padding-top: 0; }
</style>
</head>
<body>
<main class="canvas">
  <section class="business-card">
    <div class="wood-texture" role="img" aria-label="Weathered dark wood plank texture"></div>

    <div class="block block--black top-left-block"></div>
    <div class="block block--black top-right-block"></div>
    <div class="block block--white logo-extension"></div>
    <div class="block block--white logo-band">
      <div class="logo">
        <span class="logo-dot"></span>
        <span class="logo-name">Copper Lantern</span>
      </div>
    </div>

    <div class="block block--white name-band">
      <h1 class="name-title">Maureen Fitch - General Manager</h1>
    </div>

    <div class="block block--black contact-panel">
      <div class="contact-column contact-column--left">
        <p>Copper Lantern Public House</p>
        <p>58 Mill Lane Ashvale</p>
        <p>Middlesex TW9 3RK</p>
      </div>
      <div class="contact-column contact-column--right">
        <p>www.copperlanternvale.co.uk</p>
        <p>Tel: 020 7946 0382</p>
        <p>Mobile: 077009 00415</p>
      </div>
    </div>
  </section>
</main>
</body>
</html>
```